Real Estate Design Website

I would like to have a design for "real estate agent" website. It needs to be in a "Responsive" framework.

The design need to be suitable for different viewer from all around the world. It needs to be modern. It'd be great if there is a design for mobile and vexo/tablet (it's all under responsive framework). It needs to be easy to navigate and look modern

Target Market(s)

End user/Real estate buyers from different part of the world

Industry/Entity Type

Real Estate

Requirements
Must have
• It's for real estate agent website which is used to represent their brand/image but at the same time it also for their client which is real estate buyers
Should not have
• Should not be boring design/out of date

```html
<!DOCTYPE html>
<html lang="en">
<head>
<meta charset="utf-8">
<title>casaterra – Real Estate</title>
<link href="https://fonts.googleapis.com/css2?family=Open+Sans:wght@300;400;600&family=Lato:ital,wght@0,400;0,700;1,400&display=swap" rel="stylesheet">
<style>
:root{
  --green:#99cc00;
  --green-dark:#8bbb0a;
  --blue:#00b4ef;
  --blue-social:#2a9fd6;
  --navy-social:#3b5998;
  --text:#333;
  --muted:#999;
  --nav:#555;
  --row-light:#fafafa;
  --row-dark:#ececec;
  --gray-bg:#7d7d7d;
}
*{box-sizing:border-box;margin:0;padding:0}
html,body{width:1200px;height:1000px;overflow:hidden;background:#fff;font-family:"Open Sans",Arial,sans-serif;color:var(--text)}
.page{position:relative;width:1200px;height:1000px;overflow:hidden}

/* header */
.site-header{position:absolute;top:0;left:0;width:1200px;height:107px;background:#fff}
.brand{position:absolute;left:110px;top:14px;display:flex;align-items:center;gap:8px}
.brand-dot{width:34px;height:34px;border-radius:50%;background:var(--green)}
.brand-name{font-size:28px;font-weight:400;color:#333;letter-spacing:1px}
.main-nav{position:absolute;left:111px;top:62px;display:flex;height:45px}
.main-nav a{display:block;padding:0 11px;line-height:44px;font-size:15px;color:var(--nav);text-decoration:none}
.main-nav .home{width:40px;padding:0;border-bottom:3px solid var(--blue);border-right:1px dotted #bbb;display:flex;align-items:center;justify-content:center;margin-right:12px}
.social{position:absolute;top:33px;right:111px;display:flex;gap:21px}
.social span{width:40px;height:40px;border-radius:50%;display:block}
.social .s1{background:var(--blue-social)}
.social .s2{background:var(--navy-social)}
.social .s3{background:var(--blue)}

/* hero */
.hero{position:absolute;top:107px;left:0;width:1200px;height:428px;
  background:linear-gradient(90deg,#7fb6bd 0%,#9cc7cc 25%,#e4ece8 45%,#eef2ee 60%,#d7e6dc 75%,#e9eee8 90%,#b8d4dc 100%)}
.hero-toggle{position:absolute;left:381px;top:393px;width:457px;height:35px;background:var(--green);display:flex;align-items:center;justify-content:center}

/* stats */
.stats{position:absolute;top:535px;left:0;width:1200px;height:102px;background:#fff;border-bottom:2px solid #ddd}
.stat{position:absolute;top:36px;display:flex;align-items:flex-start}
.stat-icon{width:40px;height:40px;background:var(--blue);display:flex;align-items:center;justify-content:center;margin-right:12px}
.stat-title{font-size:20px;font-weight:300;color:#333;line-height:24px}
.stat-sub{font-size:11px;color:var(--muted);line-height:16px}
.stat-text{padding-right:10px;border-right:1px dotted #555}
.stat-num{font-family:"Lato",sans-serif;font-weight:700;font-size:19px;padding-left:12px;line-height:40px}

/* listings */
.listings{position:absolute;top:637px;left:0;width:1200px;height:363px;
  background:radial-gradient(ellipse at 50% 40%,#9a9a9a 0%,#7a7a7a 60%,#5e5e5e 100%)}
.card{position:absolute;top:53px;width:218px;background:#fff;font-family:"Lato",sans-serif}
.card-photo{height:125px}
.card-row{height:42px;display:flex;justify-content:space-between;align-items:center;padding:0 18px;font-size:14px}
.card-row:nth-child(odd){background:var(--row-dark)}
.card-row:nth-child(even){background:var(--row-light)}
.card-row dt{font-style:italic;color:#666;font-size:13px}
.card-row dd{font-weight:400;color:#222}
.arrow{position:absolute;top:211px;width:22px;height:39px;background:#3a3a3a;display:flex;align-items:center;justify-content:center}
.arrow.prev{left:87px;border-radius:20px 0 0 20px}
.arrow.next{left:1092px;border-radius:0 20px 20px 0}
</style>
</head>
<body>
<div class="page">
  <header class="site-header">
    <div class="brand"><span class="brand-dot"></span><span class="brand-name">casaterra</span></div>
    <nav class="main-nav">
      <a class="home" href="#" aria-label="Home"><svg width="18" height="16" viewBox="0 0 18 16"><path d="M9 1L1 8h2.5v7h4v-4h3v4h4V8H17z" fill="#222"/></svg></a>
      <a href="#">About us</a><a href="#">Developers</a><a href="#">Spaces for rent</a><a href="#">Services</a><a href="#">News</a><a href="#">Contact</a>
    </nav>
    <div class="social"><span class="s1"></span><span class="s2"></span><span class="s3"></span></div>
  </header>

  <section class="hero" role="img" aria-label="Bright modern living room with turquoise wall, television, glass partitions and garden view">
    <div class="hero-toggle"><svg width="18" height="10" viewBox="0 0 18 10"><path d="M2 9l7-7 7 7" stroke="#333" stroke-width="2" fill="none"/></svg></div>
  </section>

  <section class="stats">
    <div class="stat" style="left:112px">
      <div class="stat-icon"><svg width="14" height="20" viewBox="0 0 14 20"><path d="M7 0a7 7 0 0 0-7 7c0 5 7 13 7 13s7-8 7-13a7 7 0 0 0-7-7z" fill="#111"/><circle cx="7" cy="7" r="2.5" fill="#00b4ef"/></svg></div>
      <div class="stat-text"><div class="stat-title">Development projects</div><div class="stat-sub">NOVA18, Lumen Park, Foundry</div></div>
      <div class="stat-num">5</div>
    </div>
    <div class="stat" style="left:460px">
      <div class="stat-icon"><svg width="16" height="16" viewBox="0 0 16 16"><path d="M8 1L1 7v8h14V7z" fill="#111"/><circle cx="8" cy="10" r="2" fill="#00b4ef"/></svg></div>
      <div class="stat-text"><div class="stat-title">Space for rent</div><div class="stat-sub">NOVA18, Old Depot, factory</div></div>
      <div class="stat-num">92</div>
    </div>
    <div class="stat" style="left:768px">
      <div class="stat-icon"><svg width="18" height="16" viewBox="0 0 18 16"><path d="M9 1L5 9h8z" fill="#111"/><rect x="1" y="12" width="16" height="3" fill="#111"/></svg></div>
      <div class="stat-text"><div class="stat-title">Service</div><div class="stat-sub">Building Management, Real Estate Activity</div></div>
      <div class="stat-num">6</div>
    </div>
  </section>

  <section class="listings" role="region" aria-label="Featured properties">
    <div class="arrow prev"><svg width="8" height="12" viewBox="0 0 8 12"><path d="M6 1L1 6l5 5" stroke="#fff" stroke-width="2" fill="none"/></svg></div>

    <article class="card" style="left:131px">
      <div class="card-photo" role="img" aria-label="Seaside villa terrace with pool" style="background:linear-gradient(180deg,#5b7fa8,#8fa7b8 50%,#4c5a60)"></div>
      <dl>
        <div class="card-row"><dt>Property Type:</dt><dd>Villa</dd></div>
        <div class="card-row"><dt>Asking Price:</dt><dd>$6,890,000</dd></div>
        <div class="card-row"><dt>Rooms:</dt><dd>4 beds, 3 baths</dd></div>
        <div class="card-row"><dt>City / Town:</dt><dd>New York</dd></div>
        <div class="card-row"><dt></dt><dd></dd></div>
      </dl>
    </article>

    <article class="card" style="left:371px">
      <div class="card-photo" role="img" aria-label="Office lobby with red seating" style="background:linear-gradient(180deg,#c9c6c0,#8f8a86 55%,#a33c52 75%,#9a948c)"></div>
      <dl>
        <div class="card-row"><dt>Property Type:</dt><dd>Office Space</dd></div>
        <div class="card-row"><dt>Asking Price:</dt><dd>$3,500 / mo.</dd></div>
        <div class="card-row"><dt>Rooms:</dt><dd>0 beds, 2 baths</dd></div>
        <div class="card-row"><dt>City / Town:</dt><dd>Jersey City</dd></div>
        <div class="card-row"><dt></dt><dd></dd></div>
      </dl>
    </article>

    <article class="card" style="left:614px">
      <div class="card-photo" role="img" aria-label="Low building beside a golf course and mountains" style="background:linear-gradient(180deg,#6f9fd0,#b9c9d4 35%,#8a8a6a 60%,#5f9a3c)"></div>
      <dl>
        <div class="card-row"><dt>Property Type:</dt><dd>Office Space</dd></div>
        <div class="card-row"><dt>Asking Price:</dt><dd>$2,000,000</dd></div>
        <div class="card-row"><dt>Rooms:</dt><dd>6 beds, 4 baths</dd></div>
        <div class="card-row"><dt>City / Town:</dt><dd>New York</dd></div>
        <div class="card-row"><dt></dt><dd></dd></div>
      </dl>
    </article>

    <article class="card" style="left:854px">
      <div class="card-photo" role="img" aria-label="Modern house with lit interior at dusk" style="background:linear-gradient(180deg,#8aa3c0,#5b5046 45%,#b27a3c 65%,#4c6a2c)"></div>
      <dl>
        <div class="card-row"><dt>Property Type:</dt><dd>Villa</dd></div>
        <div class="card-row"><dt>Asking Price:</dt><dd>$7,900,000</dd></div>
        <div class="card-row"><dt>Rooms:</dt><dd>6 beds, 4 baths</dd></div>
        <div class="card-row"><dt>City / Town:</dt><dd>Jersey City</dd></div>
        <div class="card-row"><dt></dt><dd></dd></div>
      </dl>
    </article>

    <div class="arrow next"><svg width="8" height="12" viewBox="0 0 8 12"><path d="M2 1l5 5-5 5" stroke="#fff" stroke-width="2" fill="none"/></svg></div>
  </section>
</div>
</body>
</html>
```